High-End Medical Center Website Design Project

This design is part of a well thought-out project by an experienced project manager / developer. The approved wireframe is attached. Creative interpretations / suggestions based on the layout encouraged.

The design is for a new state-of-the-art medical center located in Dallas, Texas. The target audience would likely be individuals (approx. 60% female /40% male) who are the healthcare decision-makers for their families. They would likely have insurance and be inclined to seek out top-quality care.

Potential clients would choose this client over others in their industry because the medical center is physician owned, meaning it is patient-focused rather than profit-focused. The facility is brand new, featuring the latest technology. (This includes an amazing waiting room featuring WiFi and docking stations.) The physicians are hand-picked by referral only.

The look of the site should be extremely clean. We are going for a well-organized, professional look with a bit of a warm glow (interpret that however you like). Use crisp corners and the colors in the logo.

Think modern, clean with some great use of color / font.

We can get lovely photography of the medical center once construction is complete. Feel free to use an "example image" behind the Featured Area ("Physician Owned. Patient-Focused") if you like. We are open to ideas.

ONE CHANGE REQUESTED IN THE WIREFRAME:

Remove the "Connect" 1/4 page footer area and replace with a quick contact form. You may swap the "Locations" area with the form if desired. Put social media icons at the top left of the page in the top header area.

(Note: Please use social media icons that match the design rather than standard icons. We preferred not placing the icons at the top, but the client requested this. Let's not bring more attention to them than necessary.)
Updates

We're custom programming this site, so there's no need to base it on a template. Also, we would prefer not to use typical "seen everywhere" stock images.Thanks.

Industry/Entity Type

Construction

Requirements
Must have
• Follow the wireframe. This has been approved.
Nice to have
• Examples of what hover states, links or dropdowns might look like.

```html
<!DOCTYPE html>
<html lang="en">
<head>
<meta charset="utf-8">
<title>Nova Medical Center</title>
<link href="https://fonts.googleapis.com/css2?family=Source+Sans+3:ital,wght@0,400;0,600;0,700;1,400&family=Arimo:wght@400&display=swap" rel="stylesheet">
<style>
:root{
  --teal:#3aa9b5;
  --teal-dark:#2f95a0;
  --ink:#3c3c3c;
  --muted:#666;
  --rule:#d6d6d6;
  --page:#ffffff;
  --bg:#efeeec;
  --dark:#2a2a2a;
  --hero-a:#0d2f63;
  --hero-b:#2f6db3;
}
*{box-sizing:border-box;margin:0;padding:0}
html,body{width:1200px;height:1198px;overflow:hidden}
body{background:var(--bg);font-family:"Source Sans 3",Arial,sans-serif;color:var(--ink);position:relative}
.page{position:absolute;left:100px;top:0;width:1000px;height:1198px;background:var(--page);box-shadow:0 0 8px rgba(0,0,0,.08)}
.abs{position:absolute}
a{color:inherit;text-decoration:none}

.social{left:31px;top:11px;display:flex;gap:11px}
.social span{width:20px;height:20px;border-radius:50%;background:#d4d4d4;display:block}
.social span.is-active{background:var(--teal)}
.call{right:20px;top:13px;font-size:14px;color:var(--teal)}
.rule{height:1px;background:var(--rule);left:20px;width:962px}

.brand{left:20px;top:58px;height:37px;display:flex;align-items:center;gap:8px}
.brand-mark{width:30px;height:30px;background:#1f5fae}
.brand-name{font-size:22px;font-weight:700;color:#1f5fae;letter-spacing:.5px}

.nav{right:20px;top:62px;display:flex;font-family:"Arimo",Arial,sans-serif;font-size:13px;color:#444}
.nav a{height:29px;line-height:29px;padding:0 26px}
.nav a.is-current{background:var(--teal);color:#fff;padding:0 18px;margin-right:8px}

.hero{left:20px;top:122px;width:962px;height:300px;background:radial-gradient(ellipse at 45% 40%,#5a8fd0 0%,var(--hero-b) 35%,var(--hero-a) 100%);overflow:hidden;text-align:center;color:#fff}
.hero-shadow{left:60px;top:420px;width:880px;height:36px;background:radial-gradient(ellipse at 50% 0,rgba(0,0,0,.28),rgba(0,0,0,0) 70%)}
.hero h1{position:absolute;top:30px;width:100%;font-size:43px;font-weight:700}
.hero p{position:absolute;top:84px;width:100%;font-size:19px}
.hero .arrow{position:absolute;top:137px;width:43px;height:30px;background:var(--teal)}
.hero .arrow.prev{left:0;clip-path:polygon(0 0,100% 0,80% 100%,0 100%)}
.hero .arrow.next{right:0;clip-path:polygon(0 0,100% 0,100% 100%,20% 100%)}
.hero .arrow svg{position:absolute;top:8px}
.hero-icon{position:absolute;top:157px;width:98px;height:98px;border-radius:50%;border:2px solid rgba(255,255,255,.75)}
.hero-icon svg{position:absolute;left:24px;top:24px}

.tag{left:20px;top:519px;width:202px;height:42px;background:var(--teal);color:#fff;font-family:Arimo,Arial,sans-serif;font-size:18px;line-height:42px;padding-left:11px;clip-path:polygon(0 0,84% 0,100% 50%,84% 100%,0 100%)}
.feature{top:484px;width:236px}
.feature h3,.section-title{font-size:19px;font-weight:400;color:var(--teal)}
.feature p{margin-top:8px;font-size:11.5px;line-height:17px;color:#444}

.portrait{left:20px;top:696px;width:196px;height:188px;border:3px solid #d8d8d8;background:linear-gradient(180deg,#f3f3f3 0%,#dfe6ee 55%,#b9c9dc 100%)}
.about{left:234px;top:697px;width:388px}
.about p{margin-top:4px;font-size:11.5px;line-height:17px;color:#444;text-align:justify}
.about .more{display:block;font-family:Arimo,Arial,sans-serif;font-size:12px;color:var(--teal);margin-top:1px}
.testimonials{left:667px;top:695px;width:315px}
.quote{margin-top:10px;margin-left:2px;height:130px;background:var(--dark);color:#fff;font-family:Arimo,Arial,sans-serif;font-size:12px;line-height:17px;padding:20px 38px}
.quote-tail{position:absolute;right:8px;top:160px;width:48px;height:20px;background:var(--dark);clip-path:polygon(0 0,100% 0,0 100%)}
.author{text-align:right;margin-top:11px;margin-right:70px;font-size:11px;font-style:italic;color:var(--teal)}

.footer-bar{left:0;top:950px;width:1000px;height:4px;background:var(--teal)}
.col-title{top:976px;font-size:13px;color:var(--teal)}
.post{display:flex;gap:7px;width:182px;font-size:11px;line-height:14px;color:#555}
.thumb{width:40px;height:40px;border:1px solid #ccc;flex:none;background:linear-gradient(180deg,#e7e2de,#c9b8ad)}
.post em{display:block;color:#333}
.post-split{height:1px;background:#cfcfcf;width:182px;margin:6px 0 5px}
.location{left:411px;top:1003px;font-size:11px;line-height:17px;color:#444}
.location p{margin-bottom:9px}
.form{left:606px;top:1005px;width:170px}
.field{height:25px;border:2px solid #ddd;margin-bottom:6px;font-size:10px;color:#999;padding:3px 5px}
.field.tall{height:34px}
.submit{position:absolute;left:98px;top:106px;width:70px;height:24px;background:var(--teal);color:#fff;font-family:Arimo,Arial,sans-serif;font-size:11px;text-align:center;line-height:24px}
.wait{left:802px;top:981px;width:180px;height:138px;background:var(--dark);color:#fff;text-align:center;font-family:Arimo,Arial,sans-serif;padding-top:19px}
.wait h4{font-weight:400;font-size:19px}
.wait .time{font-size:21px;margin-top:6px}
.wait p{font-size:12.5px;line-height:17px;margin-top:8px}

.bottom-rule{left:0;top:1152px;width:1000px;height:1px;background:var(--rule)}
.copyright{left:20px;top:1169px;font-size:11px;color:#444}
.legal{right:20px;top:1166px;font-size:11px;color:#444}
.to-top{left:1131px;top:1164px;width:59px;height:34px;background:#4a4a4a}
</style>
</head>
<body>
<div class="page">
  <div class="abs social" aria-label="Social links"><span></span><span></span><span class="is-active"></span><span></span></div>
  <div class="abs call">Call now: (555) 014-2290</div>
  <div class="abs rule" style="top:42px"></div>

  <div class="abs brand"><span class="brand-mark"></span><span class="brand-name">NOVA MEDICAL CENTER</span></div>
  <nav class="abs nav">
    <a class="is-current" href="#">Why Nova</a><a href="#">Physicians</a><a href="#">Specialities</a><a href="#">Info</a><a href="#">Locations</a><a href="#">Contact</a>
  </nav>
  <div class="abs rule" style="top:110px"></div>

  <div class="abs hero-shadow"></div>
  <section class="abs hero" role="img" aria-label="Blurred blue photograph of the medical center interior">
    <h1>Physician Owned. Patient Focused</h1>
    <p>Lorem ipsum dolor sit amet, consectetur adipisicing elit</p>
    <span class="arrow prev"><svg width="43" height="14" viewBox="0 0 43 14" style="left:0"><path d="M20 2 L14 7 L20 12" stroke="#fff" stroke-width="2.5" fill="none"/></svg></span>
    <span class="arrow next"><svg width="43" height="14" viewBox="0 0 43 14" style="left:0"><path d="M23 2 L29 7 L23 12" stroke="#fff" stroke-width="2.5" fill="none"/></svg></span>
    <div class="hero-icon" style="left:240px"><svg width="50" height="50" viewBox="0 0 50 50" fill="none" stroke="#fff" stroke-width="4"><path d="M10 6 V20 a10 10 0 0 0 20 0 V6"/><path d="M20 30 V36 a8 8 0 0 0 16 0 V30"/><circle cx="36" cy="24" r="5"/></svg></div>
    <div class="hero-icon" style="left:409px"><svg width="50" height="50" viewBox="0 0 50 50" fill="#fff"><path d="M6 14 L34 8 L44 12 V40 L16 46 L6 42 Z"/><rect x="28" y="22" width="10" height="8" fill="#3b6fae"/></svg></div>
    <div class="hero-icon" style="left:580px"><svg width="50" height="50" viewBox="0 0 50 50" fill="#fff"><path d="M18 10 h14 v6 h-3 v-3 h-8 v3 h-3 z"/><rect x="6" y="16" width="38" height="26" rx="3"/><path d="M22 21 h6 v5 h5 v6 h-5 v5 h-6 v-5 h-5 v-6 h5 z" fill="#2f63a4"/></svg></div>
  </section>

  <div class="abs tag">Why Nova is Apart</div>
  <div class="abs feature" style="left:252px"><h3>Technology</h3><p>Lorem ipsum dolor sit amet, consectetur adipisicing elit, sed do eiusmod tempor incididunt ut labore et dolore magna aliqua. Ut enim ad minim veniam, quis nostrud exercitation .</p></div>
  <div class="abs feature" style="left:504px"><h3>Quality of Care</h3><p>Lorem ipsum dolor sit amet, consectetur adipisicing elit, sed do eiusmod tempor incididunt ut labore et dolore magna aliqua. Ut enim ad minim veniam, quis nostrud exerci ex ea.</p></div>
  <div class="abs feature" style="left:750px"><h3>Patient Experience</h3><p>Lorem ipsum dolor sit amet, consectetur adipisicing elit, sed do eiusmod tempor incididunt ut labore et dolore magna aliqua. Ut enim ad minim veniam, quis nostrud ex ea.</p></div>
  <div class="abs rule" style="top:645px"></div>

  <div class="abs portrait" role="img" aria-label="Portrait photograph of a smiling physician in shirt and tie"></div>
  <div class="abs about">
    <h2 class="section-title">About Nova</h2>
    <p>Lorem ipsum dolor sit amet, consectetur adipisicing elit, sed do eiusmod tempor incididunt ut labore et dolore magna aliqua. Ut enim ad minim veniam, quis nostrud exercitation ullamco laboris nisi ut aliquip ex ea commodo consequat. Duis aute irure dolor in reprehenderit in voluptate velit esse cillum dolore eu fugiat nulla pariatur. Excepteur sint occaecat cupidatat non proident, sunt in culpa qui officia deserunt mollit anim id est laborum.<br>Sed ut perspiciatis unde omnis iste natus error sit voluptatem accusantium doloremque laudantium, totam rem aperiam, eaque ipsa quae ab illo inventore veritatis et quasi architecto.</p>
    <a class="more" href="#">Read more</a>
  </div>
  <div class="abs testimonials">
    <h2 class="section-title">Testimonials</h2>
    <div class="quote">Sed ut perspiciatis unde omnis iste natus error sit voluptatem accusantium doloremque laudantium, totam rem aperiam, eaque ipsa quae ab illo inventore veritatis et quasi architecto beatae aut odit aut fugit,</div>
    <span class="quote-tail"></span>
    <div class="author">Daniel Marsh</div>
  </div>

  <div class="abs footer-bar"></div>
  <div class="abs col-title" style="left:20px">News</div>
  <div class="abs col-title" style="left:215px">Blog</div>
  <div class="abs col-title" style="left:411px">Location</div>
  <div class="abs col-title" style="left:606px">Quick Contact</div>

  <div class="abs" style="left:20px;top:1004px">
    <div class="post"><span class="thumb" role="img" aria-label="Author photo"></span><div>Sed ut perspiciatis unde omnis iste natus error sit<em>22January 2012</em></div></div>
    <div class="post-split"></div>
    <div class="post"><span class="thumb" role="img" aria-label="Author photo"></span><div>Sed ut perspiciatis unde omnis iste natus error sit<em>22January 2012</em></div></div>
  </div>
  <div class="abs" style="left:215px;top:1004px">
    <div class="post"><span class="thumb" role="img" aria-label="Author photo"></span><div>Sed ut perspiciatis unde omnis iste natus error sit<em>22January 2012</em></div></div>
    <div class="post-split"></div>
    <div class="post"><span class="thumb" role="img" aria-label="Author photo"></span><div>Sed ut perspiciatis unde omnis iste natus error sit<em>22January 2012</em></div></div>
  </div>

  <div class="abs location">
    <p>4820 Meadowlane Ave. Suite 210, Fairview,<br>Texas, USA, 75069</p>
    <p>Phone No: (555) 014-2290</p>
    <p>Email: hello@novamedcenter.example</p>
  </div>

  <div class="abs form">
    <div class="field">Name</div>
    <div class="field">Phone No</div>
    <div class="field tall">Comment</div>
    <span class="submit">Submit</span>
  </div>

  <div class="abs wait">
    <h4>Average Wait Time</h4>
    <div class="time">9 minutes</div>
    <p>Lorem ipsum dolor sit amet,<br>consectetur adipisicing elit.</p>
  </div>

  <div class="abs bottom-rule"></div>
  <div class="abs copyright">© Copyright 2013 · All rights reserved</div>
  <div class="abs legal">Sitemap &nbsp;|&nbsp; Privacy Policy</div>
</div>
<div class="abs to-top"><svg width="59" height="34" viewBox="0 0 59 34"><path d="M17 30 L29.5 16 L42 30" stroke="#fff" stroke-width="3" fill="none"/></svg></div>
</body>
</html>
```